Increasing performance of Security Operations Centers

Stellavant builds Security Operations Centers (SOC) that enable Pinnacle 1000 clients to be proactive and predictive in the way they secure their people and facilities. The methods involve automating threat detection, streamlining workflows, and outsourcing the most appropriate tasks. The outcomes are a reduction in total incidents and faster response times with fewer resources so clients can focus on their core business.
We're looking for 2 slides to replace the attached PPT. The first slide would be broken into each of the 8 capabilities when presenting: i.e. starting with "Reduce incidents..." on the first slide, building on with "Better direct..." on the second and continuing around clockwise. I'm looking for a more compelling way to present the capabilities and am not wedded to the way it is laid out now.
Also attached is our brand book for color and font values to comply with.

I will extend the deadline to 3/28 as soon as I figure out how.

```html
<!DOCTYPE html>
<html lang="en">
<head>
<meta charset="utf-8">
<title>SOC Performance Improvement Objectives</title>
<link href="https://fonts.googleapis.com/css2?family=Arimo:ital,wght@0,400;0,700;1,400;1,700&display=swap" rel="stylesheet">
<style>
  :root{
    --red:#BE2B27;
    --navy:#0B3F63;
    --page:#EFEFEF;
    --white:#FFFFFF;
    --text:#555555;
    --ink:#2A2A2A;
    --line:#E4E4E4;
  }
  *{box-sizing:border-box;margin:0;padding:0}
  html,body{width:978px;height:1200px;overflow:hidden;background:var(--page)}
  body{position:relative;font-family:"Arimo",Arial,sans-serif;color:var(--text)}

  .slide{position:absolute;left:42px;width:895px;height:503px;background:var(--white);
    box-shadow:0 2px 14px rgba(0,0,0,.14)}
  .slide--capabilities{top:77px}
  .slide--outcomes{top:620px}

  .title-band{position:absolute;left:0;top:21px;width:624px;height:47px;background:var(--red);
    border-radius:0 24px 24px 0;display:flex;align-items:center;padding-left:73px}
  .title-band h1{font-size:24px;font-weight:400;font-style:italic;color:var(--white);letter-spacing:-.2px}
  .brand{position:absolute;left:689px;top:26px;font-size:27px;font-weight:400;color:var(--navy);letter-spacing:-.3px}

  .pill{position:absolute;width:341px;height:72px;background:var(--white);border:1px solid var(--line);
    border-radius:36px;box-shadow:0 2px 6px rgba(0,0,0,.12);display:flex;align-items:center}
  .pill p{font-size:11.5px;line-height:19px;color:var(--text)}
  .pill--left{left:92px;justify-content:flex-end;padding-right:84px;text-align:right}
  .pill--right{left:461px;padding-left:87px}
  .pill .badge{position:absolute;top:3px;width:65px;height:65px;border-radius:50%;
    display:flex;align-items:center;justify-content:center}
  .pill--left .badge{right:3px}
  .pill--right .badge{left:3px}
  .badge--red{background:var(--red)}
  .badge--navy{background:var(--navy)}
  .badge svg{width:40px;height:40px;fill:none;stroke:var(--white);stroke-width:1.2;stroke-linecap:round;stroke-linejoin:round}

  .row1{top:104px}.row2{top:202px}.row3{top:300px}.row4{top:398px}

  .subtitle{position:absolute;left:0;width:100%;top:99px;text-align:center;font-size:19px;font-style:italic;color:var(--text)}
  .approach{position:absolute;top:145px;width:160px;text-align:center;font-size:18px;font-weight:700;font-style:italic;color:var(--ink)}
  .approach::before{content:"";display:block;width:6px;height:6px;border-radius:50%;margin:0 auto 10px;background:var(--navy)}
  .approach--red::before{background:var(--red)}
  .approach--1{left:193px}.approach--2{left:361px}.approach--3{left:529px}

  .outcome-rings{position:absolute;left:0;top:0;width:895px;height:503px}
  .outcome-label{font-family:"Arimo",Arial,sans-serif;font-size:14.5px;font-style:italic;fill:var(--text)}
  .num{font-family:"Arimo",Arial,sans-serif;font-size:14px;font-weight:700;font-style:italic;fill:var(--white)}
</style>
</head>
<body>

<section class="slide slide--capabilities">
  <div class="title-band"><h1>SOC Performance Improvement Objectives</h1></div>
  <div class="brand">Stellavant</div>

  <div class="pill pill--left row1">
    <p>Reduce incidents, respond faster, with fewer<br>resources</p>
    <div class="badge badge--navy"><svg viewBox="0 0 24 24"><path d="M3 16a9 9 0 0 1 18 0H3"/><path d="M12 8v1M7 10l.7.7M17 10l-.7.7"/><circle cx="12" cy="16" r="3.3"/><path d="M13.3 14.8 16 11.5"/><path d="M12.9 15.2c-.3-.4-1.8-.4-1.8.4s1.8.5 1.8 1.3-1.5.8-1.8.3M12 14.3v3.6"/></svg></div>
  </div>
  <div class="pill pill--left row2">
    <p>Better direct your security/safety personnel to<br>situations where they are needed most.</p>
    <div class="badge badge--red"><svg viewBox="0 0 24 24"><path d="M12 3 19 6v5c0 5-3 8-7 10-4-2-7-5-7-10V6z"/><path d="M12 5.3 17 7.5v3.5c0 3.8-2.2 6.2-5 7.7-2.8-1.5-5-3.9-5-7.7V7.5z"/><path d="m9 12 2 2 4-4"/></svg></div>
  </div>
  <div class="pill pill--left row3">
    <p>Free up time for more engagement,<br>deterrence, and investigations.</p>
    <div class="badge badge--navy"><svg viewBox="0 0 24 24"><circle cx="11" cy="12" r="4.5"/><path d="m14.3 15.3 4.5 4.5 1-1-4.5-4.5"/><path d="M9 12.5l1.5 1.2 2.5-2.7"/><circle cx="4" cy="6" r="1"/><circle cx="11" cy="4" r="1"/><circle cx="18" cy="6" r="1"/><path d="M4.8 6.6 7.7 9M11 5v2.5M17.2 6.6 14.3 9"/></svg></div>
  </div>
  <div class="pill pill--left row4">
    <p>Lessen your management burden.</p>
    <div class="badge badge--red"><svg viewBox="0 0 24 24"><circle cx="9" cy="9" r="2"/><path d="M9 4.5v1.5M9 12v1.5M4.5 9H6M12 9h1.5M5.8 5.8l1 1M11.2 11.2l1 1M5.8 12.2l1-1M11.2 6.8l1-1"/><path d="M16 5h3M16 5v8M16 9h3M16 13h3"/><circle cx="20" cy="5" r=".9"/><circle cx="20" cy="9" r=".9"/><circle cx="20" cy="13" r=".9"/><path d="M3 18h4l3 1.5h4a1 1 0 0 0 0-2h-3M3 21h6l9-3.5a1 1 0 0 0-.8-1.8L14 17"/></svg></div>
  </div>

  <div class="pill pill--right row1">
    <div class="badge badge--red"><svg viewBox="0 0 24 24"><circle cx="11" cy="4.5" r="2.3"/><path d="M11.8 3.6c-.3-.3-1.4-.3-1.4.3s1.4.4 1.4 1-1.1.6-1.4.3"/><path d="M4 11h2v9H4zM8.5 13h2v7h-2zM13 15h2v5h-2zM17.5 16h2v4h-2z"/><path d="M4 8l4 1.5 3 3 4 1 3 2.5M16.5 16.5l1.5-.5-.4-1.5"/></svg></div>
    <p>Reduce Total Cost</p>
  </div>
  <div class="pill pill--right row2">
    <div class="badge badge--navy"><svg viewBox="0 0 24 24"><circle cx="8" cy="8" r="4.5"/><path d="M3.5 8h9M8 3.5c-2 2.5-2 6.5 0 9M8 3.5c2 2.5 2 6.5 0 9"/><path d="M12 13h8v5h-8z"/><path d="M15 18l-.7 2.5h3.4L17 18"/><path d="M11 10.5h3v2.5"/></svg></div>
    <p>Outsource Key or Non-Core Functions</p>
  </div>
  <div class="pill pill--right row3">
    <div class="badge badge--red"><svg viewBox="0 0 24 24"><path d="M10 3h7v4h-7zM10 10h7v4h-7zM10 17h7v4h-7z"/><path d="M11.5 5h4M11.5 12h4M11.5 9.3"/><path d="m11.5 19 1.3 1 2.4-2.2"/><path d="M3 5h5M6.5 3.5 8 5l-1.5 1.5"/><path d="M17 5h1.5a3.5 3.5 0 0 1 0 7H17M19 11l-1.7 1 1.7 1"/><path d="M10 12H7.5a3.5 3.5 0 0 0 0 7H10M8 18l1.7 1L8 20"/></svg></div>
    <p>Automate threat detection, streamline<br>workflows</p>
  </div>
  <div class="pill pill--right row4">
    <div class="badge badge--navy"><svg viewBox="0 0 24 24" style="stroke-width:1.5"><path d="M12 3.5 21.5 20h-19z"/><path d="M12 9.5v5.5M12 17.5v.3"/></svg></div>
    <p>Increase your installed systems protective<br>usefulness &amp; adaptability to new threats</p>
  </div>
</section>

<section class="slide slide--outcomes">
  <div class="title-band"><h1>SOC Performance Improvement Objectives</h1></div>
  <div class="brand">Stellavant</div>

  <div class="subtitle">Reduce Total Cost of Operations</div>
  <div class="approach approach--1">Proactive</div>
  <div class="approach approach--2 approach--red">Predictive</div>
  <div class="approach approach--3">Preventative</div>

  <svg class="outcome-rings" viewBox="0 0 895 503" aria-label="Three outcomes: reduce incidents, respond faster, fewer resources">
    <defs>
      <filter id="soft" x="-20%" y="-20%" width="140%" height="140%">
        <feDropShadow dx="0" dy="2" stdDeviation="4" flood-color="#000" flood-opacity=".14"/>
      </filter>
    </defs>

    <!-- Outcome 01 -->
    <g>
      <circle cx="224" cy="338" r="94" fill="#fff" filter="url(#soft)"/>
      <path d="M224 242 A96 96 0 0 1 224 434" fill="none" stroke="var(--red)" stroke-width="6"/>
      <circle cx="224" cy="242" r="25" fill="#F2D5D4"/>
      <circle cx="224" cy="242" r="19" fill="var(--red)"/>
      <text class="num" x="224" y="247" text-anchor="middle">01</text>
      <g transform="translate(206 302)" fill="none" stroke="var(--navy)" stroke-width="2.2" stroke-linejoin="round" stroke-linecap="round">
        <path d="M18 2 34 30H2z"/><path d="M18 11v10M18 25.5v.5"/>
      </g>
      <text class="outcome-label" x="224" y="360" text-anchor="middle">Reduce Incidents</text>
      <circle cx="224" cy="434" r="18" fill="#fff" filter="url(#soft)"/>
      <path d="M224 429v.4M224 432.5v7" stroke="var(--red)" stroke-width="1.6" stroke-linecap="round"/>
    </g>

    <!-- Outcome 02 -->
    <g>
      <circle cx="448" cy="338" r="94" fill="#fff" filter="url(#soft)"/>
      <path d="M448 242 A96 96 0 0 1 448 434" fill="none" stroke="var(--navy)" stroke-width="6"/>
      <circle cx="448" cy="242" r="25" fill="#C9D4DE"/>
      <circle cx="448" cy="242" r="19" fill="var(--navy)"/>
      <text class="num" x="448" y="247" text-anchor="middle">02</text>
      <g transform="translate(428 302)" fill="none" stroke="var(--red)" stroke-width="1.4" stroke-linecap="round">
        <path d="M1 20a19 19 0 0 1 38 0H1"/>
        <path d="M20 4v2M9 8l1 1M31 8l-1 1"/>
        <circle cx="20" cy="20" r="7"/>
        <path d="M23 17l5-6"/>
        <path d="M22.2 17.4c-.6-.8-4-.8-4 .9s4 1 4 2.8-3.4 1.8-4 .7M20 15.5v9"/>
      </g>
      <text class="outcome-label" x="448" y="360" text-anchor="middle">Respond Faster</text>
      <circle cx="448" cy="434" r="18" fill="#fff" filter="url(#soft)"/>
      <path d="M448 429v.4M448 432.5v7" stroke="var(--navy)" stroke-width="1.6" stroke-linecap="round"/>
    </g>

    <!-- Outcome 03 -->
    <g>
      <circle cx="670" cy="338" r="94" fill="#fff" filter="url(#soft)"/>
      <path d="M670 242 A96 96 0 0 1 670 434" fill="none" stroke="var(--red)" stroke-width="6"/>
      <circle cx="670" cy="242" r="25" fill="#F2D5D4"/>
      <circle cx="670" cy="242" r="19" fill="var(--red)"/>
      <text class="num" x="670" y="247" text-anchor="middle">03</text>
      <g transform="translate(656 302)" fill="none" stroke="var(--navy)" stroke-width="1.3" stroke-linecap="round" stroke-linejoin="round">
        <circle cx="13" cy="4" r="3.5"/><circle cx="13" cy="3.3" r="1.2"/><path d="M11 6.3c.6-.9 3.4-.9 4 0"/>
        <circle cx="6" cy="13" r="4"/><path d="M7.2 11.8c-.3-.4-2.2-.4-2.2.5s2.2.5 2.2 1.3-1.8.8-2.2.3M6 10.5v5"/>
        <circle cx="20" cy="13" r="2.2"/><path d="M20 9.3v1.3M20 15.4v1.3M16.3 13h1.3M22.4 13h1.3M17.4 10.4l.9.9M21.7 14.7l.9.9M17.4 15.6l.9-.9M21.7 11.3l.9-.9"/>
        <path d="M1 20h2v7H1zM3 21h3l3 1.5h4a1 1 0 0 1 0 2h-4M3 26h6l10-3.5a1.1 1.1 0 0 0-.8-2L13 22.5"/>
      </g>
      <text class="outcome-label" x="670" y="360" text-anchor="middle">Fewer Resources</text>
      <circle cx="670" cy="434" r="18" fill="#fff" filter="url(#soft)"/>
      <path d="M670 429v.4M670 432.5v7" stroke="var(--red)" stroke-width="1.6" stroke-linecap="round"/>
    </g>
  </svg>
</section>

</body>
</html>
```